Powerpoint presentation about personal finance

Investing 4$ per day is what has been required to become a millionaire by investing in the stock market from 1965 to 2015. Yet only 1% of the population is millionaire. This presentation is about the most common causes why people do not build significant wealth through their life. We intend to educate people with this presentation, but also build trust so they become client of our wealth management firm. Feel free to send us any question about this project.
Updates

Reason: I have uploaded the logo source file and an updated PPT file. Thanks

Target Market(s)

People with a willingness to save money between the age of 20 to 50 years old

Industry/Entity Type

Finance

Font styles to use
Sans Serif

Requirements
Must have
• We are looking at uniforming the design throughout the presentation with nice, classic tone colors, large font size as it needs to be visible 3 meters apart. The content of the presentation will be updated regularly.
Should not have
• cartoon style, not serious

```html
<!DOCTYPE html>
<html lang="fr">
<head>
<meta charset="utf-8">
<title>Présentation – Finances personnelles</title>
<link href="https://fonts.googleapis.com/css2?family=Lato:wght@400;700;900&display=swap" rel="stylesheet">
<style>
  :root{
    --bg:#595959;
    --green:#12a04f;
    --green-dark:#0e8a43;
    --blue:#1a72bd;
    --blue-sky:#4a97d6;
    --ink:#2c2c2c;
    --title-blue:#1e6bb0;
    --white:#ffffff;
  }
  *{box-sizing:border-box;margin:0;padding:0}
  html,body{width:1200px;height:1008px;overflow:hidden;background:var(--bg)}
  body{position:relative;font-family:"Lato",sans-serif;color:var(--ink)}
  .preview-title{position:absolute;left:34px;top:20px;font-size:39px;font-weight:900;color:var(--white);letter-spacing:-.3px}
  .slide{position:absolute;width:360px;height:270px;background:var(--white);overflow:hidden}
  .col1{left:36px}.col2{left:422px}.col3{left:810px}
  .row1{top:91px}.row2{top:395px}.row3{top:699px}

  .strip-top{position:absolute;left:0;right:0;top:15px;height:8px;background:var(--green)}
  .footer-bar{position:absolute;left:0;top:248px;width:293px;height:7px;background:var(--blue)}
  .footer-bar span{position:absolute;left:16px;top:0;font-size:5px;line-height:7px;color:var(--white);font-weight:700}
  .footer-tail{position:absolute;right:0;top:248px;width:20px;height:7px;background:var(--blue)}
  .footer-dot{position:absolute;left:303px;top:234px;width:34px;height:34px;border-radius:50%;border:3px solid var(--blue);background:var(--white)}

  .brand{display:flex;align-items:center;gap:6px;font-weight:900;color:var(--blue)}
  .brand i{display:block;border-radius:50%;border:3px solid var(--blue)}

  .caps{font-variant:small-caps;text-transform:none}
  .header{position:absolute;left:0;right:0;top:0;background:var(--green);color:var(--white);font-weight:700;text-align:center;display:flex;align-items:center;justify-content:center}

  /* slide 1 */
  .s1-photo{position:absolute;left:0;top:0;width:360px;height:189px;background:linear-gradient(160deg,#5aa4de,#3f8ccf 60%,#4b95d5)}
  .s1-text{position:absolute;left:40px;right:40px;top:66px;text-align:center;color:var(--white);font-size:16.5px;line-height:21.5px}
  .s1-brand{position:absolute;left:112px;top:207px;font-size:22px}
  .s1-brand i{width:38px;height:38px}
  .s1-base{position:absolute;left:0;right:0;bottom:0;height:6px;background:var(--green)}

  /* slide 2 */
  .s2-top{position:absolute;left:0;right:0;top:0;height:12px;background:var(--green)}
  .s2-photo{position:absolute;left:0;top:12px;width:360px;height:243px;background:radial-gradient(circle at 50% 55%,#3f8fd0,#2273b8 70%,#1d68a8)}
  .s2-band{position:absolute;left:0;right:0;top:105px;height:60px;background:rgba(255,255,255,.86);display:flex;align-items:center;justify-content:center;color:var(--title-blue);font-weight:700;font-size:22px}
  .s2-logo{position:absolute;left:118px;top:215px;width:134px;height:40px;background:var(--white);display:flex;align-items:center;justify-content:center}
  .s2-logo .brand{font-size:14px}.s2-logo i{width:24px;height:24px;border-width:2px}
  .s2-base{position:absolute;left:0;right:0;bottom:0;height:15px;background:var(--green)}

  /* slide 3 */
  .s3-text{position:absolute;left:48px;right:48px;top:78px;font-size:20px;line-height:24px;color:#333;text-align:justify}

  /* slide 4 */
  .s4-head{height:50px;font-size:9.5px;line-height:12px;padding:0 20px}
  .chart{position:absolute;left:0;top:50px}

  /* slide 5 */
  .s5-text{position:absolute;left:49px;right:47px;top:58px;font-size:17.5px;line-height:21.6px;text-align:justify;color:#333}

  /* bullets */
  .header.small{height:36px;font-size:13px}
  .list{list-style:none}
  .list li{position:relative;padding-left:14px;text-align:justify}
  .list li::before{content:"";position:absolute;left:1px;top:.5em;width:4px;height:4px;background:var(--green)}
  .s6-list{position:absolute;left:20px;right:18px;top:51px;font-size:11.2px;line-height:14.4px}
  .s6-list li{margin-bottom:14.5px}

  /* slide 7 */
  .s7-photo{position:absolute;left:0;top:0;width:360px;height:225px;background:linear-gradient(150deg,#2fae62,#1f9c53 50%,#35b069)}
  .s7-title{position:absolute;left:0;right:0;top:37px;text-align:center;color:var(--white);font-weight:700;font-size:15.5px}
  .s7-text{position:absolute;left:44px;right:38px;top:74px;color:var(--white);font-size:13.5px;line-height:16.8px;text-align:justify}
  .s7-text p+p{margin-top:14px}

  /* slide 8 */
  .s8-intro{position:absolute;left:19px;right:19px;top:41px;font-size:11.5px;line-height:14.4px;text-align:justify}
  .s8-list{position:absolute;left:20px;right:19px;top:87px;font-size:11.5px;line-height:14.4px}
  .s8-list li{text-align:left}

  /* slide 9 */
  .s9-q{position:absolute;left:0;right:0;top:56px;text-align:center;color:var(--green-dark);font-weight:700;font-size:12.5px}
  .s9-body{position:absolute;left:20px;right:19px;top:86px;font-size:12.5px;line-height:15.6px}
  .s9-body .list{margin:8px 0 9px 2px}
  .s9-body .list li{margin-bottom:.5px}
  .s9-body p{text-align:justify}
</style>
</head>
<body>
  <h1 class="preview-title">PPT Slides Preview</h1>

  <!-- Slide 1 -->
  <section class="slide col1 row1">
    <div class="s1-photo" role="img" aria-label="Photo de fond bleue de billets de banque"></div>
    <p class="s1-text caps">L’idéal pour nous tous n’est-il pas d’avoir suffisamment d’argent et d’être en santé afin de pouvoir réaliser nos rêves?</p>
    <div class="brand s1-brand"><i></i>Cendral</div>
    <div class="s1-base"></div>
  </section>

  <!-- Slide 2 -->
  <section class="slide col2 row1">
    <div class="s2-top"></div>
    <div class="s2-photo" role="img" aria-label="Photo bleue d’une rosace vue en gros plan"></div>
    <div class="s2-band caps">Quels sont vos rêves?</div>
    <div class="s2-logo"><div class="brand"><i></i>Cendral</div></div>
    <div class="s2-base"></div>
  </section>

  <!-- Slide 3 -->
  <section class="slide col3 row1">
    <div class="strip-top"></div>
    <p class="s3-text caps">Malheureusement, ce n’est pas tout le monde qui ont la chance de réaliser tous leurs rêves, pourtant ceci est à la portée de presque tous…</p>
    <div class="footer-bar"><span>© CENDRAL 2016</span></div><div class="footer-dot"></div><div class="footer-tail"></div>
  </section>

  <!-- Slide 4 -->
  <section class="slide col1 row2">
    <div class="header s4-head">Investissement fixe équivalent à 4$ par jour dans les actions pour un individu né en 1950 et qui a commencé à épargner à 15 ans</div>
    <svg class="chart" width="360" height="200" viewBox="0 50 360 200" font-family="Lato, sans-serif" font-size="7" fill="#333">
      <defs>
        <pattern id="grid" width="10" height="5.625" patternUnits="userSpaceOnUse" y="65">
          <line x1="0" y1="0" x2="10" y2="0" stroke="#d4d4d4" stroke-width=".6"/>
        </pattern>
      </defs>
      <rect x="72" y="65" width="266" height="135" fill="url(#grid)"/>
      <line x1="72" y1="65" x2="72" y2="200" stroke="#999" stroke-width=".7"/>
      <line x1="72" y1="200" x2="338" y2="200" stroke="#999" stroke-width=".7"/>
      <g text-anchor="end">
        <text x="60" y="68">1,200,000 $</text>
        <text x="60" y="90.5">1,000,000 $</text>
        <text x="60" y="113">800,000 $</text>
        <text x="60" y="135.5">600,000 $</text>
        <text x="60" y="158">400,000 $</text>
        <text x="60" y="180.5">200,000 $</text>
        <text x="60" y="203">- $</text>
      </g>
      <ellipse cx="31" cy="110.5" rx="13" ry="5.5" fill="none" stroke="#d62020" stroke-width="1"/>
      <polyline fill="none" stroke="#3b6fc4" stroke-width="1.8" stroke-linejoin="round"
        points="72,200 98.6,199.7 125,199 152,198 168,197 178,195.5 189,193 200,190 210,187 216,182 221,183 226,178 232,176 237,174 242,173 248,165 253,156 258,111 264,121 269,148 274,128 280,126 285,117 290,114 296,148 301,127 306,127 312,115 317,87 322,73 328,74"/>
      <g font-size="7" text-anchor="end">
        <text transform="translate(77,210) rotate(-45)">1965</text>
        <text transform="translate(93,210) rotate(-45)">1968</text>
        <text transform="translate(109,210) rotate(-45)">1971</text>
        <text transform="translate(125,210) rotate(-45)">1974</text>
        <text transform="translate(141,210) rotate(-45)">1977</text>
        <text transform="translate(157,210) rotate(-45)">1980</text>
        <text transform="translate(173,210) rotate(-45)">1983</text>
        <text transform="translate(189,210) rotate(-45)">1986</text>
        <text transform="translate(205,210) rotate(-45)">1989</text>
        <text transform="translate(221,210) rotate(-45)">1992</text>
        <text transform="translate(237,210) rotate(-45)">1995</text>
        <text transform="translate(253,210) rotate(-45)">1998</text>
        <text transform="translate(269,210) rotate(-45)">2001</text>
        <text transform="translate(285,210) rotate(-45)">2004</text>
        <text transform="translate(301,210) rotate(-45)">2007</text>
        <text transform="translate(317,210) rotate(-45)">2010</text>
        <text transform="translate(333,210) rotate(-45)">2013</text>
      </g>
    </svg>
    <div class="footer-bar"><span>© CENDRAL 2016</span></div><div class="footer-dot"></div><div class="footer-tail"></div>
  </section>

  <!-- Slide 5 -->
  <section class="slide col2 row2">
    <div class="strip-top"></div>
    <p class="s5-text">Pourquoi y a-t-il si peu de gens qui sont millionnaires aujourd’hui quand l’équivalent de 4$ par jour d’économies investis dans la bourse de 1950 à 2015 a généré un portefeuille de plus de 1 million de dollars?</p>
    <div class="footer-bar"><span>© CENDRAL 2016</span></div><div class="footer-dot"></div><div class="footer-tail"></div>
  </section>

  <!-- Slide 6 -->
  <section class="slide col3 row2">
    <div class="header small">Le constat…</div>
    <ul class="list s6-list">
      <li>80% des familles québécoises ont accumulé moins de 300,000$ d’épargne.</li>
      <li>C’est donc dire que la majorité des familles s’expose à une précarité financière.</li>
      <li>L’industrie financière ne s’intéresse peu aux familles ayant moins de 250,000$ d’épargne parce qu’elle ne les trouve pas rentables.</li>
      <li>L’industrie financière échoue donc dans son devoir d’assister les familles dans l’atteinte de leurs objectifs financiers.</li>
    </ul>
    <div class="footer-bar"><span>© CENDRAL 2016</span></div><div class="footer-dot"></div><div class="footer-tail"></div>
  </section>

  <!-- Slide 7 -->
  <section class="slide col1 row3">
    <div class="s7-photo" role="img" aria-label="Photo verte d’un arbre dans un champ"></div>
    <h2 class="s7-title">Notre projet</h2>
    <div class="s7-text">
      <p>Notre projet, d’ordre social, est d’aider les familles à maximiser leur indépendance financière à long terme en partageant notre savoir et notre expertise.</p>
      <p>Votre succès deviendra donc notre succès!</p>
    </div>
    <div class="footer-bar"><span>© CENDRAL 2016</span></div><div class="footer-dot"></div><div class="footer-tail"></div>
  </section>

  <!-- Slide 8 -->
  <section class="slide col2 row3">
    <div class="strip-top"></div>
    <p class="s8-intro">Les principaux facteurs qui nuisent à l’atteinte de l’indépendance financière:</p>
    <ul class="list s8-list">
      <li>L’inaction et le report à plus tard</li>
      <li>Les erreurs émotives (la peur)</li>
      <li>Favoriser les plaisirs à court terme plutôt que les bénéfices à long terme</li>
      <li>Le manque de connaissances</li>
      <li>L’accès à l’information</li>
      <li style="text-align:justify">Les frais de gestion et la rémunération des conseiller financiers</li>
      <li>Les impôts</li>
      <li>L’inflation</li>
    </ul>
    <div class="footer-bar"><span>© CENDRAL 2016</span></div><div class="footer-dot"></div><div class="footer-tail"></div>
  </section>

  <!-- Slide 9 -->
  <section class="slide col3 row3">
    <div class="header small">L’inaction…</div>
    <p class="s9-q">Vous croyez ne pas avoir les moyens d’épargner?</p>
    <div class="s9-body">
      <p>Pour générer 4$ par jour, il suffit:</p>
      <ul class="list">
        <li>faire son café à la maison au lieu de l’acheter sur la route</li>
        <li>Faire son lunch au lieu de manger au restaurant</li>
        <li>Réduire le nombre de chaînes sur votre abonnement au câble</li>
      </ul>
      <p>Bref il est possible d’y arriver sans réduire son style de vie de façon significative!</p>
    </div>
    <div class="footer-bar"><span>© CENDRAL 2016</span></div><div class="footer-dot"></div><div class="footer-tail"></div>
  </section>
</body>
</html>
```